Cole Varga Photography

Would like the Business card to have a cool logo. I’m targeting wedding/ engagement: portrait photography. My phone number on it. And my business email address.

Wedding/portrait/engagement photography.

```html
<!DOCTYPE html>
<html lang="en">
<head>
<meta charset="utf-8">
<title>Cole Varga Photography – Business Card</title>
<link href="https://fonts.googleapis.com/css2?family=Cinzel:wght@500&family=Montserrat:wght@400&family=Arimo:wght@400&display=swap" rel="stylesheet">
<style>
  :root {
    --backdrop: #3a3a3a;
    --card-dark: #1b1b1b;
    --gold: #f0b424;
    --gold-deep: #c98a08;
    --ink: #1a1408;
    --white: #ffffff;
    --sky-top: #6b5212;
    --sky-mid: #d9a71c;
    --sky-glow: #f8d85a;
    --shore: #2a1f05;
  }
  * { margin: 0; padding: 0; box-sizing: border-box; }
  html, body {
    width: 1200px; height: 1015px; overflow: hidden;
    background: var(--backdrop);
  }
  .canvas {
    width: 1200px; height: 1015px;
    display: flex; flex-direction: column; align-items: center; justify-content: center;
    gap: 56px;
  }
  .card {
    width: 700px; height: 400px; position: relative; overflow: hidden;
    box-shadow: 0 14px 30px rgba(0,0,0,.45);
  }

  /* Front */
  .card-front .scene {
    position: absolute; inset: 0;
    background:
      radial-gradient(ellipse 60% 45% at 62% 18%, var(--sky-glow) 0%, rgba(248,216,90,0) 70%),
      linear-gradient(180deg, var(--sky-top) 0%, var(--sky-mid) 45%, #b8870f 62%, #e9b928 70%, var(--shore) 100%);
  }
  .front-logo {
    position: absolute; left: 160px; top: 150px;
    display: flex; flex-direction: column; align-items: flex-start;
  }
  .brand-name {
    font-family: 'Cinzel', serif; font-weight: 500;
    font-size: 56px; letter-spacing: 3px; line-height: 1;
    display: flex; align-items: center; gap: 14px;
  }
  .brand-dot { width: 22px; height: 22px; border-radius: 50%; flex: none; }
  .brand-tag {
    font-family: 'Montserrat', sans-serif; font-weight: 400;
    font-size: 19px; letter-spacing: 9px; margin-top: 10px; margin-left: 4px;
  }
  .card-front .brand-name, .card-front .brand-tag { color: var(--ink); }
  .card-front .brand-dot { background: var(--ink); }

  /* Back */
  .card-back { background: var(--card-dark); }
  .back-logo { position: absolute; left: 70px; top: 80px; }
  .card-back .brand-name, .card-back .brand-tag { color: var(--gold); }
  .card-back .brand-dot { background: var(--gold); }
  .holder-name {
    position: absolute; left: 74px; top: 232px;
    font-family: 'Cinzel', serif; font-weight: 500;
    font-size: 22px; letter-spacing: 1px; color: var(--gold);
  }
  .contact-list {
    position: absolute; left: 74px; top: 276px; list-style: none;
    display: flex; flex-direction: column; gap: 8px;
  }
  .contact-item {
    display: flex; align-items: center; gap: 10px;
    font-family: 'Arimo', sans-serif; font-size: 19px; color: var(--white);
  }
  .contact-icon { width: 22px; height: 22px; flex: none; }
</style>
</head>
<body>
<main class="canvas">
  <section class="card card-front">
    <div class="scene" role="img" aria-label="Golden sunset over the sea with a couple silhouetted beside a beach umbrella and loungers"></div>
    <div class="front-logo">
      <div class="brand-name"><span>COLE VARGA</span><span class="brand-dot"></span></div>
      <div class="brand-tag">PHOTOGRAPHY</div>
    </div>
  </section>

  <section class="card card-back">
    <div class="back-logo">
      <div class="brand-name"><span>COLE VARGA</span><span class="brand-dot"></span></div>
      <div class="brand-tag">PHOTOGRAPHY</div>
    </div>
    <div class="holder-name">DANIEL HART</div>
    <ul class="contact-list">
      <li class="contact-item">
        <svg class="contact-icon" viewBox="0 0 22 22" aria-hidden="true">
          <circle cx="11" cy="11" r="9.5" fill="none" stroke="var(--gold)" stroke-width="2"/>
          <path d="M7.5 6.5c-.8.8-.6 3 1.6 5.3s4.6 2.6 5.4 1.8l.6-.8-1.8-1.4-.9.7c-.8-.3-2.2-1.6-2.5-2.5l.7-.9L9.2 6.9z" fill="var(--gold)"/>
        </svg>
        <span>555-214-3080</span>
      </li>
      <li class="contact-item">
        <svg class="contact-icon" viewBox="0 0 22 22" aria-hidden="true">
          <circle cx="11" cy="11" r="9.5" fill="none" stroke="var(--gold)" stroke-width="2"/>
          <rect x="6" y="7.5" width="10" height="7" fill="var(--gold)"/>
          <path d="M6 7.5l5 4 5-4" fill="none" stroke="var(--card-dark)" stroke-width="1"/>
        </svg>
        <span>hello@colevarga.com</span>
      </li>
      <li class="contact-item">
        <svg class="contact-icon" viewBox="0 0 22 22" aria-hidden="true">
          <circle cx="11" cy="11" r="9.5" fill="none" stroke="var(--gold)" stroke-width="2"/>
          <circle cx="11" cy="11" r="5" fill="none" stroke="var(--gold)" stroke-width="1.4"/>
          <path d="M6 11h10M11 6c-2 3-2 7 0 10M11 6c2 3 2 7 0 10" fill="none" stroke="var(--gold)" stroke-width="1.1"/>
        </svg>
        <span>www.colevarga.com</span>
      </li>
    </ul>
  </section>
</main>
</body>
</html>
```